Creative Challenge - Disruptive Digital Construction Business needs an Application Design

We need an application design (4 screens).
The app will offer easy-to-use an interactive course to illustrate the latest technology to construction professionals. Kindly find the attachments.
Updates

I have just posted the contest and the deadline is tomorrow!! Please give me my original 7 days back.

Need extra days to review

Target Market(s)

Construction professionals, aged from 22 to 36, who want to learn new disruptive technologies in construction.

Colors
e667a6
b868aa
33a6d7

Requirements
Must have
• The name of the app, Velunor, stands for “Brightframe Skill Voyagers”. The user is a Velunor, who would transform the digital construction industry. We want a design that gives that feel to the users.

```html
<!DOCTYPE html>
<html lang="en">
<head>
<meta charset="utf-8">
<title>Velunor – App Screens</title>
<link href="https://fonts.googleapis.com/css2?family=Mulish:wght@400;600;700;800&display=swap" rel="stylesheet">
<style>
:root{
  --night:#0b0c1e;
  --paper:#f7f7fb;
  --card:#ffffff;
  --ink:#1d1d2b;
  --muted:#6c6c7a;
  --line:#33a6d7;
  --blue:#33a6d7;
  --pink:#e667a6;
  --violet:#b868aa;
  --blush:#fbc4dd;
  --blush-soft:#fdeef5;
  --shade:#57575c;
  --green:#7ccfa6;
  --yellow:#f2d15a;
}
*{box-sizing:border-box;margin:0;padding:0}
html,body{width:1200px;height:1149px;overflow:hidden;background:var(--night)}
body{font-family:"Mulish",sans-serif;color:var(--ink)}
.board{position:absolute;left:0;top:0;width:1960px;height:1876px;transform:scale(.6122);transform-origin:0 0}
.screen{position:absolute;width:220px;height:483px;border-radius:18px;background:var(--paper);overflow:hidden}
.screen--tall{height:966px}
.screen > *{position:absolute}
.status{top:4px;left:12px;right:12px;height:10px;font-size:7px;display:flex;justify-content:space-between;align-items:center}
.status i{display:inline-block;width:24px;height:5px;background:linear-gradient(90deg,var(--ink) 0 8px,transparent 8px 11px,var(--ink) 11px 14px,transparent 14px 16px,var(--ink) 16px);border-radius:1px}
.art{border-radius:50%}
.t{font-size:7px;line-height:1.35;white-space:nowrap}
.label{font-size:8px;color:var(--muted)}
.value{font-size:7.5px;font-weight:600}
.rule{height:1px;background:var(--line)}
.btn{display:flex;align-items:center;justify-content:center;font-size:8px;border-radius:2px}
.btn--solid{background:var(--blue);color:#fff}
.btn--ghost{border:1px solid var(--blue);color:var(--blue)}
.chev{width:5px;height:5px;border-right:1.2px solid var(--ink);border-bottom:1.2px solid var(--ink);transform:rotate(45deg)}
.chev--up{transform:rotate(-135deg)}
.chev--right{transform:rotate(-45deg)}
.toggle{width:24px;height:12px;border-radius:6px;background:#e3e3e8}
.toggle::after{content:"";position:absolute;top:1px;left:1px;width:10px;height:10px;border-radius:50%;background:#bbb}
.toggle--on{background:var(--blue)}
.toggle--on::after{left:13px;background:#fff}
.panel{background:var(--card);border-radius:3px;box-shadow:0 1px 3px rgba(0,0,0,.06)}
.dot{width:4px;height:4px;border-radius:50%}
.step{left:8px;width:207px;height:32px;background:var(--card);border-right:3px solid var(--pink);border-radius:3px;display:flex;align-items:center;font-size:7px;line-height:1.3;overflow:hidden}
.step b{flex:none;width:28px;height:32px;display:flex;align-items:center;justify-content:center;font-size:5.5px;font-weight:600;background:radial-gradient(circle at 0 0,var(--blush) 0 16px,transparent 17px)}
.menu-row{left:12px;display:flex;align-items:center;gap:10px;font-size:8px}
.ico{width:11px;height:11px;border:1.3px solid var(--ink);border-radius:50%}
.para{font-size:7.8px;line-height:1.45;color:var(--muted);white-space:normal}
</style>
</head>
<body>
<main class="board">

<!-- Onboarding -->
<section class="screen" style="left:150px;top:157px">
  <div class="status"><span>9:41</span><i></i></div>
  <div class="art" role="img" aria-label="Illustration of a businessman seated on a stack of books beside a small construction crane" style="left:35px;top:73px;width:160px;height:165px;background:radial-gradient(circle at 55% 45%,#eef0f6 0 55%,transparent 56%),linear-gradient(180deg,transparent 60%,#c44f8c 60% 85%,transparent 85%)"></div>
  <div style="top:290px;left:0;width:220px;text-align:center;font-size:12px;font-weight:700;line-height:1.3">Lorem dolor sit amet<br>consectetur adipisicing elit</div>
  <div class="t" style="top:345px;left:0;width:220px;text-align:center;font-size:6.5px;color:var(--muted)">Lorem dolor sit amet consectetur adipisicing eli<br>sed do eiusmod tempor</div>
  <div style="top:403px;left:93px;display:flex;gap:6px;align-items:center"><span class="dot" style="background:var(--ink)"></span><span class="dot" style="width:6px;height:6px;background:var(--ink)"></span><span class="dot" style="background:var(--ink)"></span><span class="dot" style="background:var(--ink)"></span></div>
  <div class="t" style="top:437px;right:8px;font-size:7px">SKIP</div>
</section>

<!-- Welcome -->
<section class="screen" style="left:511px;top:157px">
  <div class="status"><span>9:41</span><i></i></div>
  <div class="art" role="img" aria-label="Illustration of a man working on a laptop in a pink egg chair" style="left:34px;top:58px;width:150px;height:185px;background:radial-gradient(circle at 50% 40%,#e9e9f3 0 55%,transparent 56%),radial-gradient(ellipse at 45% 50%,#c44f8c 0 30%,transparent 31%)"></div>
  <div style="top:278px;left:0;width:220px;text-align:center;font-size:21px">Welcome</div>
  <div class="t" style="top:317px;left:0;width:220px;text-align:center;font-size:6.5px;color:var(--muted)">Please login or sign up to continue<br>using this app</div>
  <div class="btn btn--solid" style="top:368px;left:21px;width:80px;height:26px">Login</div>
  <div class="btn btn--ghost" style="top:368px;left:117px;width:81px;height:26px">Signup</div>
</section>

<!-- Login -->
<section class="screen" style="left:871px;top:157px">
  <div class="status"><span>9:41</span><i></i></div>
  <div class="t" style="top:72px;left:10px;font-size:8px">Welcome to</div>
  <div class="t" style="top:87px;left:10px;font-size:10px">Brightframe Skill Voyagers</div>
  <div style="top:108px;left:10px;font-size:20px;font-weight:800;color:var(--blue)">Velunor</div>
  <div class="label" style="top:166px;left:10px">Email</div>
  <div class="value" style="top:186px;left:10px">username@velunor.app</div>
  <svg style="top:186px;left:197px" width="9" height="9" viewBox="0 0 10 10"><circle cx="5" cy="3" r="2.3" fill="#1d1d2b"/><path d="M1 10a4 4 0 0 1 8 0z" fill="#1d1d2b"/></svg>
  <div class="rule" style="top:203px;left:10px;width:199px"></div>
  <div class="label" style="top:213px;left:10px">Password</div>
  <div class="value" style="top:231px;left:10px;letter-spacing:1.5px">••••••••••</div>
  <svg style="top:233px;left:196px" width="12" height="8" viewBox="0 0 12 8"><ellipse cx="6" cy="4" rx="6" ry="4" fill="#1d1d2b"/><circle cx="6" cy="4" r="1.8" fill="#fff"/></svg>
  <div class="rule" style="top:249px;left:10px;width:199px"></div>
  <div class="t" style="top:255px;right:11px;font-size:6.5px;color:var(--blue)">Forgot Password?</div>
  <div class="btn btn--solid" style="top:287px;left:10px;width:199px;height:25px">Login</div>
  <div style="top:352px;left:10px;width:199px;height:1px;background:#cfcfd6"></div>
  <div class="t" style="top:346px;left:80px;padding:0 4px;background:var(--paper);font-size:6.5px">Or Signup With</div>
  <div style="top:376px;left:37px;width:24px;height:24px;border:1px solid var(--ink);border-radius:50%"></div>
  <div style="top:376px;left:98px;width:24px;height:24px;border:1px solid var(--ink);border-radius:50%"></div>
  <div style="top:376px;left:158px;width:24px;height:24px;border:1px solid var(--ink);border-radius:50%"></div>
  <div class="t" style="top:420px;left:0;width:220px;text-align:center;font-size:6.5px">New Member? <span style="color:var(--blue)">Sign up</span></div>
</section>

<!-- Signup -->
<section class="screen" style="left:1232px;top:157px">
  <div class="status"><span>9:41</span><i></i></div>
  <div style="top:26px;left:10px;width:10px;height:10px;border-radius:50%;background:#777"></div>
  <div style="top:20px;left:0;width:220px;text-align:center;font-size:16px;font-weight:800;color:var(--blue)">Velunor</div>
  <div class="label" style="top:53px;left:10px">Name</div><div class="value" style="top:71px;left:10px">username</div><div class="rule" style="top:85px;left:10px;width:199px"></div>
  <div class="label" style="top:96px;left:10px">Email</div><div class="value" style="top:114px;left:10px">username@velunor.app</div><div class="rule" style="top:128px;left:10px;width:199px"></div>
  <div class="label" style="top:139px;left:10px">Mobile Number</div><div class="value" style="top:157px;left:10px">username</div><div class="rule" style="top:171px;left:10px;width:199px"></div>
  <div class="label" style="top:182px;left:10px">Password</div><div class="value" style="top:198px;left:10px;letter-spacing:1.5px">••••••••••</div><div class="rule" style="top:214px;left:10px;width:199px"></div>
  <div class="label" style="top:224px;left:10px">Gender</div><div class="value" style="top:242px;left:10px">Select</div><div class="chev" style="top:242px;left:190px"></div><div class="rule" style="top:256px;left:10px;width:199px"></div>
  <div class="label" style="top:267px;left:10px">Country of Residence</div><div class="value" style="top:285px;left:10px">Select country</div><div class="chev" style="top:285px;left:190px"></div><div class="rule" style="top:299px;left:10px;width:199px"></div>
  <div class="label" style="top:310px;left:10px">Company</div><div class="value" style="top:328px;left:10px">Company name</div><div class="rule" style="top:342px;left:10px;width:199px"></div>
  <div class="label" style="top:353px;left:10px">Title</div><div class="value" style="top:371px;left:10px">Title here</div><div class="rule" style="top:385px;left:10px;width:199px"></div>
  <div class="label" style="top:396px;left:10px">Years of Experience</div><div class="value" style="top:414px;left:10px">Select here</div><div class="chev" style="top:413px;left:190px"></div><div class="rule" style="top:428px;left:10px;width:199px"></div>
  <div class="btn btn--solid" style="top:442px;left:10px;width:199px;height:25px">Signup</div>
</section>

<!-- Role filter -->
<section class="screen" style="left:1593px;top:157px;background:var(--shade)">
  <div style="top:26px;left:10px;width:10px;height:8px;border-top:1.3px solid #222;border-bottom:1.3px solid #222"></div>
  <div style="top:29px;left:10px;width:10px;height:1.3px;background:#222"></div>
  <div style="top:26px;left:198px;width:11px;height:8px;border-top:1px solid #222;border-bottom:1px solid #222"></div>
  <div style="top:54px;left:3px;width:214px;height:354px;background:var(--card)"></div>
  <div style="top:60px;left:198px;font-size:12px">✕</div>
  <div class="t" style="top:93px;left:10px;font-size:7.5px">Show All</div><div class="toggle toggle--on" style="top:92px;left:184px"></div>
  <div class="t" style="top:121px;left:10px;font-size:7.5px">I am the client (Appointing Party)</div><div class="toggle" style="top:120px;left:184px"></div>
  <div class="t" style="top:149px;left:10px;font-size:7.5px">I am the lead consultant/<br>lead contractor/<br>lead PM, etc (Lead Appoined Party)</div><div class="toggle toggle--on" style="top:149px;left:184px"></div>
  <div class="t" style="top:199px;left:10px;font-size:7.5px">I am the consultant/subcontractot/<br>supplier, etc. (Appointed Party)</div><div class="toggle" style="top:199px;left:184px"></div>
  <div class="art" role="img" aria-label="Illustration of a businessman seated on a stack of pink books" style="left:60px;top:250px;width:100px;height:110px;background:radial-gradient(circle at 50% 40%,#eef0f6 0 50%,transparent 51%),linear-gradient(180deg,transparent 58%,#c44f8c 58% 85%,transparent 85%)"></div>
  <div style="top:374px;left:0;width:220px;text-align:center;font-size:10px;color:#444">Customize your Journey</div>
</section>

<!-- Home -->
<section class="screen screen--tall" style="left:150px;top:779px">
  <div class="status"><span>9:41</span><i></i></div>
  <div style="top:27px;left:12px;width:10px;height:9px;border-top:1.3px solid var(--ink);border-bottom:1.3px solid var(--ink)"></div>
  <div style="top:31px;left:12px;width:10px;height:1.3px;background:var(--ink)"></div>
  <div style="top:24px;left:0;width:220px;text-align:center;font-size:10.5px;font-weight:700">Hello User!</div>
  <div style="top:27px;left:198px;width:11px;height:9px;border-top:1px solid var(--ink);border-bottom:1px solid var(--ink)"></div>
  <div class="panel" style="top:56px;left:10px;width:200px;height:32px"></div>
  <div class="btn btn--solid" style="top:60px;left:20px;width:44px;height:24px;font-size:10px">New</div>
  <div class="t" style="top:68px;left:76px;font-size:7px">Explore 6 more resources</div><div class="chev" style="top:68px;left:190px"></div>
  <div class="panel" style="top:100px;left:10px;width:200px;height:32px"></div>
  <div class="t" style="top:112px;left:20px">How to start BIM?</div><div class="chev chev--right" style="top:114px;left:188px"></div>
  <div class="panel" style="top:148px;left:10px;width:200px;height:32px"></div>
  <div class="t" style="top:159px;left:20px">Important ISO19650 principles to know</div><div class="chev chev--up" style="top:163px;left:190px"></div>
  <div class="panel" style="top:198px;left:10px;width:96px;height:84px;border-bottom:3px solid var(--pink);background:radial-gradient(circle at 12px 10px,var(--blush-soft) 0 28px,#fff 29px)"></div>
  <div class="t" style="top:245px;left:54px;font-size:7.5px;line-height:1.1">PAS 1192<br><span style="font-size:4px">vs</span><br>ISO 19650</div>
  <div class="panel" style="top:198px;left:114px;width:96px;height:84px;border-bottom:3px solid var(--blue);background:radial-gradient(circle at 12px 10px,#eef6fb 0 28px,#fff 29px)"></div>
  <div class="t" style="top:246px;left:150px;font-size:7.5px;line-height:1.3">Who are the<br>actors?</div>
  <div class="panel" style="top:292px;left:10px;width:96px;height:84px;border-bottom:3px solid var(--pink);background:radial-gradient(circle at 12px 10px,var(--blush-soft) 0 28px,#fff 29px)"></div>
  <div class="t" style="top:340px;left:24px;font-size:7.5px;line-height:1.1">Project level<br><span style="font-size:4px">vs</span><br>Appointment level</div>
  <div class="panel" style="top:292px;left:114px;width:96px;height:84px;border-bottom:3px solid var(--blue);background:radial-gradient(circle at 12px 10px,#eef6fb 0 28px,#fff 29px)"></div>
  <div class="t" style="top:340px;left:150px;font-size:7.5px;line-height:1.3">Information<br>Stages</div>
  <div class="panel" style="top:390px;left:10px;width:200px;height:36px"></div>
  <div class="t" style="top:398px;left:20px">Information Management Processes &amp;<br>Activities</div><div class="chev" style="top:404px;left:192px"></div>
  <div style="top:442px;left:23px;width:0;height:250px;border-left:1px dashed #aaa"></div>
  <div class="dot" style="top:440px;left:21px;background:var(--pink)"></div>
  <div class="t" style="top:437px;left:32px">Information Requirement Stage</div><div class="chev" style="top:438px;left:192px"></div>
  <div class="t" style="top:452px;left:32px;font-size:6px;color:var(--muted)">Project level</div>
  <div class="t" style="top:472px;left:32px;font-size:6px">5.1 Assessment &amp; Need</div>
  <div class="t" style="top:472px;left:158px;font-size:5.5px">Progress: 10%</div>
  <div style="top:487px;left:30px;width:170px;height:3px;border-radius:2px;background:linear-gradient(90deg,var(--pink) 0 12%,var(--blush) 12%)"></div>
  <div class="btn" style="top:505px;left:33px;width:53px;height:16px;background:var(--pink);color:#fff;font-size:6.5px">Explore</div>
  <div class="btn" style="top:505px;left:101px;width:60px;height:16px;border:1px solid var(--blush);color:var(--pink);font-size:6.5px">View all</div>
  <div class="dot" style="top:553px;left:21px;background:var(--green)"></div>
  <div class="t" style="top:549px;left:32px">Information Procurement Stage</div><div class="chev chev--up" style="top:553px;left:192px"></div>
  <div class="t" style="top:564px;left:32px;font-size:6px;color:var(--muted)">Appointment Level</div>
  <div class="dot" style="top:597px;left:21px;background:var(--violet)"></div>
  <div class="t" style="top:593px;left:32px">Information Planning Stage</div><div class="chev chev--up" style="top:597px;left:192px"></div>
  <div class="t" style="top:608px;left:32px;font-size:6px;color:var(--muted)">Appointment Level</div>
  <div class="dot" style="top:641px;left:21px;background:var(--yellow)"></div>
  <div class="t" style="top:637px;left:32px">Information Delivery Stage</div><div class="chev chev--up" style="top:641px;left:192px"></div>
  <div class="t" style="top:652px;left:32px;font-size:6px;color:var(--muted)">Appointment Level</div>
  <div class="dot" style="top:684px;left:21px;background:var(--blue)"></div>
  <div class="t" style="top:680px;left:32px">Information Archving Stage</div><div class="chev chev--up" style="top:684px;left:192px"></div>
  <div class="t" style="top:695px;left:32px;font-size:6px;color:var(--muted)">Project level</div>
  <div class="panel" style="top:731px;left:10px;width:200px;height:36px"></div>
  <div class="t" style="top:737px;left:20px">Documents/Resources You Need to<br>Develop</div><div class="chev" style="top:743px;left:192px"></div>
  <div style="top:780px;left:23px;width:0;height:160px;border-left:1px dashed #aaa"></div>
  <div class="dot" style="top:778px;left:21px;background:#4a5bb0"></div>
  <div class="t" style="top:775px;left:32px">To be created by the Appointing Party</div><div class="chev" style="top:776px;left:192px"></div>
  <div class="t" style="top:801px;left:42px;font-size:7.5px">Used for Information Only</div><div class="chev chev--right" style="top:804px;left:158px"></div>
  <div class="t" style="top:825px;left:42px;font-size:7.5px">Appointment Document</div><div class="chev chev--right" style="top:828px;left:158px"></div>
  <div class="dot" style="top:870px;left:21px;background:#4a5bb0"></div>
  <div class="t" style="top:867px;left:32px">To be created by the Lead Appointed<br>Party</div><div class="chev" style="top:869px;left:192px"></div>
  <div class="t" style="top:905px;left:42px;font-size:7.5px">Used for Information Only</div><div class="chev chev--right" style="top:908px;left:158px"></div>
  <div class="t" style="top:929px;left:42px;font-size:7.5px">Appointment Document</div><div class="chev chev--right" style="top:932px;left:158px"></div>
</section>

<!-- Step list -->
<section class="screen" style="left:511px;top:779px">
  <div class="status"><span>9:41</span><i></i></div>
  <div style="top:26px;left:10px;width:10px;height:10px;border-radius:50%;background:#777"></div>
  <div style="top:24px;left:0;width:220px;text-align:center;font-size:10.5px;font-weight:700">5.1 Assessment &amp; Need</div>
  <div class="step" style="top:54px;background:var(--blush-soft)"><b>5.1.1</b><span>Appoint individuals to undertake<br>information management function</span></div>
  <div class="step" style="top:95px"><b>5.1.2</b><span>Establish the Project Information<br>Requirements</span></div>
  <div class="step" style="top:136px"><b>5.1.3</b><span>Establish the project’s information<br>delivery milestones</span></div>
  <div class="step" style="top:177px"><b>5.1.4</b><span>Establish the project’s information<br>standards</span></div>
  <div class="step" style="top:218px"><b>5.1.5</b><span>Establish the project’s information<br>production methods and procedures</span></div>
  <div class="step" style="top:259px"><b>5.1.6</b><span>Establish the project’s reference<br>information and shared resource</span></div>
  <div class="step" style="top:300px"><b>5.1.7</b><span>Establish the project’s common data<br>environment</span></div>
  <div class="step" style="top:341px"><b>5.1.8</b><span>Establish the project’s information<br>protocol</span></div>
</section>

<!-- Lesson video -->
<section class="screen" style="left:871px;top:779px">
  <div role="img" aria-label="Video still of a lecturer standing beside a whiteboard" style="top:0;left:0;width:220px;height:117px;background:linear-gradient(90deg,#4a3a30 0%,#7a6a5c 35%,#e9eef0 60%,#f4f6f7 100%)"></div>
  <div class="chev" style="top:22px;left:14px;transform:rotate(135deg);border-color:#fff"></div>
  <div style="top:50px;left:100px;width:16px;height:16px;border-radius:50%;background:#fff;opacity:.9"></div>
  <svg style="top:54px;left:106px" width="6" height="8" viewBox="0 0 6 8"><path d="M0 0l6 4-6 4z" fill="#e667a6"/></svg>
  <div class="panel" style="top:128px;left:7px;width:206px;height:242px"></div>
  <div style="top:139px;left:7px;width:2px;height:20px;background:var(--pink)"></div>
  <div class="t" style="top:139px;left:16px;font-size:6px;color:var(--muted)">5.1 Assessment &amp; Need<br>Actor: The Appointing Party</div>
  <div style="top:168px;left:7px;width:2px;height:22px;background:var(--pink)"></div>
  <div class="t" style="top:168px;left:16px;font-size:8px;line-height:1.3">Appoint Individuals to undertake the<br>information management function.</div>
  <div class="para" style="top:202px;left:16px;width:190px">labore et dolore magna aliquyam erat, sed diam voluptua. At vero eos et accusam et justo duo dolores et ea rebum. Stet clita kasd gubergren, no sea takimata sanctus.</div>
  <div class="para" style="top:256px;left:16px;width:190px">Lorem ipsum dolor sit amet, consetetur sadipscing elitr, sed diam nonumy eirmod tempor invidunt ut labore et dolore magna aliquyam erat, sed diam voluptua. At vero eos et accusam et justo duo.</div>
  <div class="t" style="top:352px;left:176px;font-size:7px">Start →</div>
  <div class="t" style="top:392px;left:16px;font-size:8px;font-weight:600">Attachments</div>
  <div class="panel" style="top:408px;left:7px;width:206px;height:24px"></div>
  <div style="top:415px;left:16px;width:7px;height:9px;background:var(--pink);border-radius:1px"></div>
  <div class="t" style="top:414px;left:31px;font-size:8px">Lorem ipsum dolor sit amet</div>
  <div class="t" style="top:413px;left:192px;font-size:8px;color:var(--blue)">⤓</div>
  <div class="panel" style="top:437px;left:7px;width:206px;height:24px"></div>
  <div style="top:444px;left:16px;width:7px;height:9px;background:var(--pink);border-radius:1px"></div>
  <div class="t" style="top:443px;left:31px;font-size:8px">Lorem ipsum dolor sit amet</div>
  <div class="t" style="top:442px;left:192px;font-size:8px;color:var(--blue)">⤓</div>
</section>

<!-- Lesson reader -->
<section class="screen" style="left:1232px;top:779px">
  <div style="top:0;left:0;width:220px;height:102px;background:var(--blush)"></div>
  <div class="status"><span>9:41</span><i></i></div>
  <div style="top:21px;left:10px;width:10px;height:10px;border-radius:50%;background:#777"></div>
  <div class="t" style="top:35px;left:22px;font-size:6px;color:#555">5.1 Assessment &amp; Need</div>
  <div class="t" style="top:48px;left:22px;font-size:6px;color:#555">Actor: The Appointing Party</div>
  <div class="t" style="top:63px;left:22px;font-size:8.5px;line-height:1.35">Appoint Individuals to undertake the<br>information management function.</div>
  <div role="img" aria-label="Photo of a tower under construction wrapped in scaffolding" style="top:116px;left:14px;width:195px;height:94px;background:linear-gradient(90deg,#c9d6dc 0%,#8ea7b0 35%,#6fb7bd 65%,#bcd7de 100%)"></div>
  <div class="para" style="top:224px;left:16px;width:192px">labore et dolore magna aliquyam erat, sed diam voluptua. At vero eos et accusam et justo duo dolores et ea rebum. Stet clita kasd gubergren, no sea takimata sanctus.</div>
  <div class="para" style="top:278px;left:16px;width:192px">Lorem ipsum dolor sit amet, consetetur sadipscing elitr, sed diam nonumy eirmod mpor invidunt ut labore et dolore magna aliquyam erat, sed diam voluptua. At vero eos et accusam et justo duo.</div>
  <div class="para" style="top:344px;left:16px;width:192px">Lorem ipsum dolor sit amet, consetetur sadipscing elitr, sed diam nonumy eirmod tempor invidunt ut labore et dolore magna aliquyam erat, sed diam voluptua. At vero eos et accusam et justo duo.</div>
  <div class="t" style="top:446px;right:14px;font-size:4.5px;color:var(--muted)">Added to favorite</div>
  <div class="t" style="top:465px;left:12px;font-size:9px">🌡︎</div>
  <div class="chev" style="top:471px;left:82px;transform:rotate(135deg)"></div>
  <div class="t" style="top:467px;left:104px;font-size:8px"><b>01</b> / 30</div>
  <div class="chev chev--right" style="top:471px;left:151px"></div>
  <svg style="top:466px;left:200px" width="9" height="11" viewBox="0 0 9 11"><path d="M0 0h9v11l-4.5-3L0 11z" fill="#1d1d2b"/></svg>
</section>

<!-- Drawer -->
<section class="screen" style="left:1593px;top:779px;background:var(--shade)">
  <div style="top:0;left:0;width:190px;height:483px;background:var(--paper)"></div>
  <div style="top:0;left:0;width:190px;height:90px;background:var(--blue)"></div>
  <div class="t" style="top:18px;right:40px;font-size:6.5px;font-weight:700;color:#fff">Velunor</div>
  <div role="img" aria-label="User avatar" style="top:30px;left:12px;width:24px;height:24px;border-radius:50%;background:#8b5a44"></div>
  <div class="t" style="top:62px;left:12px;font-size:8px;font-weight:600;color:#fff">User Name</div>
  <div class="menu-row" style="top:104px"><svg width="11" height="12" viewBox="0 0 11 12"><path d="M1 1h9v10l-4.5-3L1 11z" fill="none" stroke="#1d1d2b" stroke-width="1.2"/></svg>My favorite</div>
  <div class="menu-row" style="top:131px"><svg width="11" height="11" viewBox="0 0 11 11"><circle cx="4.5" cy="4.5" r="3.5" fill="none" stroke="#1d1d2b" stroke-width="1.2"/><path d="M7 7l3.5 3.5" stroke="#1d1d2b" stroke-width="1.2"/></svg>Search</div>
  <div style="top:153px;left:0;width:190px;height:22px;background:#f0f0f5"></div>
  <div class="menu-row" style="top:158px"><span class="ico"></span>About the app</div>
  <div class="menu-row" style="top:185px"><span class="ico"></span>About the authors</div>
  <div class="menu-row" style="top:212px"><span class="ico"></span>Activity</div>
  <div class="menu-row" style="top:239px"><svg width="11" height="12" viewBox="0 0 11 12"><path d="M2 9V5a3.5 3.5 0 0 1 7 0v4l1 1H1z M4.5 11h2" fill="none" stroke="#1d1d2b" stroke-width="1.2"/></svg>Notification</div>
  <div class="toggle toggle--on" style="top:239px;left:150px"></div>
  <div class="menu-row" style="top:267px"><span class="ico" style="border-style:dashed"></span>Setting</div>
  <div class="menu-row" style="top:443px;color:var(--muted)"><svg width="12" height="10" viewBox="0 0 12 10"><path d="M5 1H1v8h4M4 5h7M8 2l3 3-3 3" fill="none" stroke="#888" stroke-width="1.1"/></svg>Log out</div>
</section>

</main>
</body>
</html>
```